Professional banners for an eyewear company

I have 3 images which need to be made into banners. Size 990 x 370, with a 10 pixel white border at top and bottom of banner.

They all need to be adjusted to make the colours better and less bright.
All will need some writing written on them with a nice serif font.

Banner 1 text: Handcrafted luxury eyewear, with a purpose...
Banner 2 text: Half of our profits go to help malnourished children in India
Banner 3 text: 10% of your first order, use code: First Order

On our homepage these 3 banners will alternate, so they need to look good together.

Tips
Please take a look at the banners on the lunvoreck.com homepage, this is kind of how I want the text to be displayed, and they use good colours.

The backgrounds on Banners 2 & 3 can be changed.
Banner 3 background if you can change to a nice colour, as per lunvoreck.com homepage.
Updates

Hi, just a quick update, thank you for all the designs submitted so far, please keep in mind that the brand is a luxury high-end brand so designs will need to reflect this.

Industry/Entity Type

Eyewear

```html
<!DOCTYPE html>
<html lang="en">
<head>
<meta charset="utf-8">
<title>Eyewear Homepage Banners</title>
<link rel="stylesheet" href="https://fonts.googleapis.com/css2?family=Arimo:wght@400;700&display=swap">
<style>
  :root {
    --page-bg: #ffffff;
    --peach-light: #fffdfb;
    --peach: #fde3cc;
    --accent-red: #e0474c;
    --grey-dark: #d8d9db;
    --grey-light: #f2f2f2;
    --grey-text-strong: #555659;
    --grey-text: #68696c;
    --gold: #f7da96;
    --brown: #7a4e12;
    --brown-soft: #9a6f35;
    --cream: #fff4dc;
  }
  * { margin: 0; padding: 0; box-sizing: border-box; }
  html, body {
    width: 1200px; height: 1000px; overflow: hidden;
    background: var(--page-bg);
    font-family: "Arimo", Arial, sans-serif;
  }
  .canvas { position: relative; width: 1200px; height: 1000px; }
  .banner { position: absolute; left: 248px; width: 704px; overflow: hidden; }

  /* Banner 1 — handcrafted eyewear */
  .banner--craft {
    top: 65px; height: 296px;
    background: linear-gradient(115deg, var(--peach-light) 0%, #fdeee0 35%, var(--peach) 75%);
  }
  .product-photo {
    position: absolute; left: 48px; top: 62px; width: 330px; height: 180px;
    background: radial-gradient(ellipse at 50% 50%, #d9c8b4 0%, #4a4240 45%, #161313 75%, rgba(22,19,19,0) 100%);
    border-radius: 40px;
  }
  .craft-copy {
    position: absolute; left: 380px; width: 306px; top: 133px;
    text-align: center; color: var(--accent-red); font-size: 16px; line-height: 21px;
  }
  .craft-copy strong { font-size: 17px; font-weight: 700; display: block; }

  /* Banner 2 — giving back */
  .banner--purpose {
    top: 373px; height: 277px;
    background: linear-gradient(200deg, #fbfbfb 0%, var(--grey-light) 25%, var(--grey-dark) 70%);
  }
  .purpose-copy {
    position: absolute; left: 85px; width: 300px; top: 107px;
    text-align: center; font-size: 16px; line-height: 20px; font-weight: 700;
    color: var(--grey-text);
  }
  .purpose-copy .lead { color: var(--grey-text-strong); display: block; }
  .child-photo {
    position: absolute; left: 430px; top: 0; width: 210px; height: 277px;
    background: linear-gradient(180deg, #6e5544 0%, #a87b62 35%, #8fb52c 60%, #7ca325 100%);
  }

  /* Banner 3 — first order offer */
  .banner--offer {
    top: 662px; height: 278px;
    background: linear-gradient(90deg, var(--gold) 0%, var(--gold) 70%, #fbecc8 85%, #ffffff 100%);
  }
  .offer-figure {
    position: absolute; left: 135px; top: 68px;
    color: var(--brown); font-weight: 700;
  }
  .offer-figure .amount { font-size: 94px; line-height: 80px; letter-spacing: -5px; display: inline-block; }
  .offer-figure .unit {
    position: absolute; left: 92px; top: 4px; width: 50px; text-align: center;
  }
  .offer-figure .percent { display: block; font-size: 44px; line-height: 42px; }
  .offer-figure .off { display: block; font-size: 22px; line-height: 24px; }
  .offer-copy {
    position: absolute; left: 110px; width: 190px; top: 153px;
    text-align: center; color: var(--brown-soft); font-size: 17px; line-height: 20px;
  }
  .offer-copy strong { display: block; font-weight: 700; }
  .order-button {
    position: absolute; left: 162px; top: 201px; width: 87px; height: 18px;
    background: var(--brown); color: var(--cream);
    font-size: 13px; line-height: 18px; text-align: center; text-decoration: none;
  }
  .model-photo {
    position: absolute; left: 300px; top: 0; width: 268px; height: 278px;
    background: linear-gradient(180deg, #b8663a 0%, #d9a58a 35%, #efe9e4 65%, #f4f0ec 100%);
  }
</style>
</head>
<body>
<main class="canvas">
  <section class="banner banner--craft">
    <div class="product-photo" role="img" aria-label="Photo of a pair of black handcrafted eyeglass frames"></div>
    <p class="craft-copy"><strong>Handcrafted luxury eyewear,</strong>with a purpose...</p>
  </section>

  <section class="banner banner--purpose">
    <p class="purpose-copy"><span class="lead">Half of our profits</span>go to help malnourished children<br>in India</p>
    <div class="child-photo" role="img" aria-label="Photo of a smiling young girl in a green top"></div>
  </section>

  <section class="banner banner--offer">
    <div class="offer-figure">
      <span class="amount">10</span>
      <span class="unit"><span class="percent">%</span><span class="off">OFF</span></span>
    </div>
    <p class="offer-copy"><strong>your first order,</strong>use code: First Order</p>
    <a class="order-button" href="#">order now &gt;&gt;</a>
    <div class="model-photo" role="img" aria-label="Photo of a red-haired woman wearing sunglasses and a polka-dot blouse"></div>
  </section>
</main>
</body>
</html>
```